Interactive Tailored Suit and Shirt Website Needs Homepage Redesign

We need our homepage redesigned. Our current website is dated and we need a refresh. We are a Melbourne based business selling tailored suits and shirts in store and online. The homepage should be fashion forward. Our colour scheme has traditionally been black and white but would interested in new ideas.
Our current website is quillora.com.au

```html
<!DOCTYPE html>
<html lang="en">
<head>
<meta charset="utf-8">
<title>Quillora – Tailored suits</title>
<link href="https://fonts.googleapis.com/css2?family=Roboto+Condensed:wght@400;700&family=Open+Sans:wght@400;600;700&display=swap" rel="stylesheet">
<style>
:root{
  --orange:#d5490a;
  --orange-light:#ee6a22;
  --dark:#2b2b2b;
  --darker:#1f1f1f;
  --text:#333;
  --muted:#666;
  --line:#dcdcdc;
  --beige:#efebe4;
  --white:#fff;
}
*{margin:0;padding:0;box-sizing:border-box}
html,body{width:924px;height:1200px;overflow:hidden;background:var(--white)}
body{position:relative;font-family:"Open Sans",Arial,sans-serif;color:var(--text)}
.abs{position:absolute}
.cond{font-family:"Roboto Condensed","Arial Narrow",sans-serif}

/* top bar */
.topbar{left:0;top:0;width:924px;height:31px;background:var(--dark)}
.logo{left:178px;top:5px;font:700 17px "Roboto Condensed",sans-serif;color:var(--orange)}
.toplinks{right:178px;top:0;height:31px;display:flex;font:600 7px "Open Sans",sans-serif;color:var(--white)}
.toplinks span{padding:0 10px;line-height:31px;border-left:1px solid #444}
.toplinks span:first-child{border-left:0}

/* nav */
.nav{left:178px;top:49px;display:flex;gap:0;font:400 9px "Roboto Condensed",sans-serif;color:var(--text)}
.nav span{margin-right:36px}
.nav .active{color:var(--orange);border-bottom:1px dashed var(--orange);padding-bottom:3px}
.nav .caret{color:var(--orange);font-size:7px}
.cart{left:650px;top:47px;width:49px;height:17px;background:#eee;border-radius:2px;font:400 7px "Open Sans",sans-serif;color:#555;line-height:17px;padding-left:24px}
.cart i{position:absolute;left:5px;top:4px;width:10px;height:9px;background:var(--orange);border-radius:1px}
.checkout{left:703px;top:47px;width:42px;height:17px;background:var(--orange);border-radius:2px;color:var(--white);font:400 7px "Open Sans",sans-serif;text-align:center;line-height:17px}

/* hero */
.hero{left:0;top:81px;width:924px;height:317px;background:linear-gradient(90deg,#8e8e8e 0%,#a9a9aa 45%,#bebec0 80%,#b2b2b4 100%)}
.hero-photo{left:533px;top:81px;width:200px;height:317px;background:linear-gradient(180deg,#3a3a3c 0%,#1e1e20 60%,#2a2a2c 100%);border-radius:40px 40px 0 0}
.hero-title{left:178px;top:131px;width:270px;font:700 19px/1.25 "Roboto Condensed",sans-serif;color:var(--dark)}
.hero-title em{font-style:normal;color:var(--orange)}
.hero-copy{left:178px;top:200px;width:250px;font:400 11px/1.3 "Roboto Condensed",sans-serif;color:#333}
.btn{background:linear-gradient(#ee6a22,#c8440a);color:var(--white);border-radius:3px;text-align:center;font-family:"Roboto Condensed",sans-serif;font-weight:700}
.shop-now{left:178px;top:311px;width:59px;height:25px;line-height:25px;font-size:8px}
.hero-rule{left:0;top:398px;width:924px;height:5px;background:var(--orange)}

/* featured */
.featured{left:0;top:403px;width:924px;height:155px;background:var(--beige);border-bottom:1px solid var(--line)}
.sec-head{font:400 11px "Roboto Condensed",sans-serif}
.feat-head{left:178px;top:416px;color:var(--orange)}
.brand-head{left:594px;top:416px;color:var(--dark)}
.thumb{top:441px;width:92px;height:85px;background:linear-gradient(180deg,#2a2a2a,#111 70%,#3a3a3a)}
.thumb-label{top:535px;width:92px;text-align:center;font:400 7px "Open Sans",sans-serif;color:#333}
.brand-box{left:594px;top:441px;width:151px;height:86px;background:var(--orange);color:var(--white);font:400 18px/86px "Roboto Condensed",sans-serif;text-align:center}

/* listing */
.list-head{left:178px;top:571px;font:700 12px "Roboto Condensed",sans-serif;color:var(--orange)}
.view-all{right:178px;top:574px;font:400 7px "Open Sans",sans-serif;color:#333}
.view-all b{color:#333;margin-right:5px;font-size:6px}
.filters{left:178px;top:596px;width:146px;height:167px;border:1px solid var(--line)}
.select{left:185px;width:132px;height:22px;border:1px solid #e2e2e2;background:linear-gradient(#fafafa,#eee);font:400 7px/20px "Open Sans",sans-serif;color:#777;padding-left:7px}
.select i{position:absolute;right:0;top:0;width:17px;height:20px;border-left:1px solid #e2e2e2}
.select i:after{content:"";position:absolute;left:5px;top:8px;border:3px solid transparent;border-top:4px solid #999}
.color-btn{left:215px;top:730px;width:75px;height:22px;line-height:22px;font-size:8px;font-weight:400}
.side-head{left:178px;font:700 11px "Roboto Condensed",sans-serif;color:var(--dark)}
.store{left:178px;width:146px;height:47px;background:var(--dark);color:var(--white)}
.store .name{position:absolute;left:7px;top:12px;font:700 11px "Roboto Condensed",sans-serif}
.store .sub{position:absolute;left:7px;top:26px;font:400 7px "Open Sans",sans-serif;color:#ddd}
.store .price{position:absolute;right:0;top:0;width:45px;height:47px;background:var(--orange);border-left:2px dashed var(--dark);padding:7px 0 0 6px;font:400 6px "Open Sans",sans-serif}
.store .price b{display:block;font:400 13px "Roboto Condensed",sans-serif;color:#ffd9c4;margin-top:2px}
.promo{left:178px;top:941px;width:146px;height:104px;background:var(--dark);color:var(--white);font:400 8px/1.3 "Open Sans",sans-serif;text-align:center;padding-top:40px}

.search{left:341px;top:596px;width:404px;height:30px;border:1px solid var(--line)}
.search-field{left:375px;top:604px;width:272px;height:15px;border:1px solid #ccc}
.search-btn{left:667px;top:603px;width:71px;height:17px;background:linear-gradient(#f7f7f7,#e6e6e6);border:1px solid #d8d8d8;font:400 8px/15px "Open Sans",sans-serif;text-align:center;color:#333}

.card{width:127px;height:135px;border:1px solid #e4e4e4;padding:3px}
.card .photo{width:100%;height:100%;background:linear-gradient(180deg,#8a8a8a,#6c6c6c);position:relative}
.card .photo.dark{background:linear-gradient(180deg,#3c3c3c,#262626)}
.card .photo.light{background:linear-gradient(180deg,#bdbdbd,#9d9d9d)}
.price-tag{position:absolute;left:0;bottom:3px;width:30px;height:15px;background:var(--dark);color:var(--white);font:400 7px/15px "Open Sans",sans-serif;text-align:center}
.actions{position:absolute;left:30px;bottom:3px;display:flex;height:15px}
.actions span{background:var(--orange);border-left:1px solid #f08a5a;height:15px;width:22px;position:relative}
.actions .details{width:43px;color:var(--white);font:400 6px/15px "Open Sans",sans-serif;text-align:center}
.card-title{width:127px;font:700 10px "Roboto Condensed",sans-serif;color:var(--orange)}
.card-desc{width:127px;font:400 6.5px/1.3 "Open Sans",sans-serif;color:#333}
.rule{left:341px;width:404px;height:1px;background:var(--line)}
.page{top:1061px;width:17px;height:16px;border:1px solid #ddd;background:#f7f7f7;font:400 7px/14px "Open Sans",sans-serif;text-align:center;color:#555}
.page.current{background:var(--orange);color:var(--white);border-color:var(--orange)}
.more{left:703px;top:1061px;width:42px;height:16px;border:1px solid #ddd;background:#f7f7f7;font:400 7px/14px "Open Sans",sans-serif;color:#555;padding-left:7px}

/* footer */
.footer{left:0;top:1108px;width:924px;height:63px;background:var(--dark)}
.foot-links{left:178px;top:1135px;font:400 6.5px "Open Sans",sans-serif;color:var(--white);letter-spacing:.2px}
.social{top:1119px;width:20px;height:20px;border-radius:50%}
.copyright{left:0;top:1171px;width:924px;height:29px;background:var(--orange);color:var(--white);font:400 7px/29px "Open Sans",sans-serif;padding-left:180px}
.chat{left:564px;top:1132px;width:182px;height:68px;background:var(--orange)}
.chat-tab{left:696px;top:1111px;width:50px;height:22px;background:var(--orange);border-radius:3px 3px 0 0}
.chat-input{left:579px;top:1148px;width:154px;height:22px;background:var(--white);font:400 6.5px/22px "Open Sans",sans-serif;color:#777;padding-left:6px}
</style>
</head>
<body>

<header>
  <div class="abs topbar"></div>
  <div class="abs logo">Quillora</div>
  <nav class="abs toplinks"><span>Sign in</span><span>Order History / Reorder</span><span>Contact us</span><span>Customer help</span></nav>
  <nav class="abs nav"><span class="active">Home</span><span>About</span><span>Shope <b class="caret">▼</b></span><span>what is new</span></nav>
  <div class="abs cart"><i></i>0 item</div>
  <div class="abs checkout">Check out</div>
</header>

<section>
  <div class="abs hero"></div>
  <div class="abs hero-photo" role="img" aria-label="Model in a dark pinstripe suit with tie and pocket square"></div>
  <h1 class="abs hero-title">Quillora <em>of Branded suiting for the modern man.</em></h1>
  <p class="abs hero-copy">We have suits for all occasions, from the business suit to the dapper special occasion suits to wedding and black tie hire</p>
  <div class="abs btn shop-now">SHOP NOW</div>
  <div class="abs hero-rule"></div>
</section>

<section>
  <div class="abs featured"></div>
  <h2 class="abs sec-head feat-head">Featured items</h2>
  <h2 class="abs sec-head brand-head">Top Selling Brands</h2>
  <div class="abs thumb" style="left:178px" role="img" aria-label="Man in black suit and sunglasses"></div>
  <div class="abs thumb" style="left:282px" role="img" aria-label="Man in black suit and sunglasses"></div>
  <div class="abs thumb" style="left:386px" role="img" aria-label="Man in black suit and sunglasses"></div>
  <div class="abs thumb" style="left:490px" role="img" aria-label="Man in black suit and sunglasses"></div>
  <div class="abs thumb-label" style="left:178px">Item Name</div>
  <div class="abs thumb-label" style="left:282px">Item Name</div>
  <div class="abs thumb-label" style="left:386px">Item Name</div>
  <div class="abs thumb-label" style="left:490px">Item Name</div>
  <div class="abs brand-box">BRAND NAME</div>
</section>

<main>
  <h2 class="abs list-head">Top Selling items</h2>
  <div class="abs view-all"><b>➜</b>View all items</div>

  <aside>
    <div class="abs filters"></div>
    <div class="abs select" style="top:604px">Select by Product Categories<i></i></div>
    <div class="abs select" style="top:633px">Select by Style<i></i></div>
    <div class="abs select" style="top:661px">Select by Color<i></i></div>
    <div class="abs select" style="top:690px">Select by Size<i></i></div>
    <div class="abs btn color-btn">View all color</div>

    <h3 class="abs side-head" style="top:776px">What's hot</h3>
    <div class="abs store" style="top:802px"><span class="name">WOMEN STORE</span><span class="sub">Women T shirts</span><div class="price">Start From<b>$50</b></div></div>
    <div class="abs store" style="top:855px"><span class="name">MEN STORE</span><span class="sub">Men T shirts</span><div class="price">Start From<b>$50</b></div></div>

    <h3 class="abs side-head" style="top:914px">Permotion</h3>
    <div class="abs promo">251 x 181<br>Permotaional Area</div>
  </aside>

  <div class="abs search"></div>
  <svg class="abs" style="left:349px;top:605px" width="11" height="11" viewBox="0 0 11 11"><circle cx="4.5" cy="4.5" r="3.3" fill="none" stroke="#bbb" stroke-width="1.3"/><line x1="7" y1="7" x2="10" y2="10" stroke="#bbb" stroke-width="1.5"/></svg>
  <div class="abs search-field"></div>
  <div class="abs search-btn">Search</div>

  <!-- row 1 -->
  <div class="abs card" style="left:340px;top:642px"><div class="photo light" role="img" aria-label="Man in grey suit">
    <div class="price-tag">$250</div>
    <div class="actions">
      <span><svg class="abs" style="left:6px;top:3px" width="10" height="9" viewBox="0 0 10 9"><path d="M0 1h2l1.2 5h5l1-3.5H3" fill="none" stroke="#fff" stroke-width="1"/><circle cx="4" cy="8" r=".9" fill="#fff"/><circle cx="7.5" cy="8" r=".9" fill="#fff"/></svg></span>
      <span><svg class="abs" style="left:6px;top:3px" width="10" height="9" viewBox="0 0 10 9"><path d="M5 8.5L1 4.5A2.2 2.2 0 0 1 5 1.8 2.2 2.2 0 0 1 9 4.5z" fill="#fff"/></svg></span>
      <span class="details">View Details</span>
    </div></div></div>
  <div class="abs card" style="left:478px;top:642px"><div class="photo" role="img" aria-label="Man in charcoal suit"><div class="price-tag">$250</div></div></div>
  <div class="abs card" style="left:617px;top:642px"><div class="photo" role="img" aria-label="Man in charcoal suit"><div class="price-tag">$250</div></div></div>
  <div class="abs card-title" style="left:340px;top:789px">Item Name Goes Here</div>
  <div class="abs card-title" style="left:478px;top:789px">Item Name Goes Here</div>
  <div class="abs card-title" style="left:617px;top:789px">Item Name Goes Here</div>
  <p class="abs card-desc" style="left:340px;top:803px">Lorem Ipsum is simply dummy text of the print ndar</p>
  <p class="abs card-desc" style="left:478px;top:803px">Lorem Ipsum is simply dummy text of the print ndar</p>
  <p class="abs card-desc" style="left:617px;top:803px">Lorem Ipsum is simply dummy text of the print ndar</p>
  <div class="abs rule" style="top:836px"></div>

  <!-- row 2 -->
  <div class="abs card" style="left:340px;top:851px"><div class="photo dark" role="img" aria-label="Man in navy suit with checked tie"><div class="price-tag">$250</div></div></div>
  <div class="abs card" style="left:478px;top:851px"><div class="photo dark" role="img" aria-label="Man in navy suit with checked tie"><div class="price-tag">$250</div></div></div>
  <div class="abs card" style="left:617px;top:851px"><div class="photo dark" role="img" aria-label="Man in navy suit with checked tie"><div class="price-tag">$250</div></div></div>
  <div class="abs card-title" style="left:340px;top:998px">Item Name Goes Here</div>
  <div class="abs card-title" style="left:478px;top:998px">Item Name Goes Here</div>
  <div class="abs card-title" style="left:617px;top:998px">Item Name Goes Here</div>
  <p class="abs card-desc" style="left:340px;top:1012px">Lorem Ipsum is simply dummy text of the print ndar</p>
  <p class="abs card-desc" style="left:478px;top:1012px">Lorem Ipsum is simply dummy text of the print ndar</p>
  <p class="abs card-desc" style="left:617px;top:1012px">Lorem Ipsum is simply dummy text of the print ndar</p>
  <div class="abs rule" style="top:1045px"></div>

  <nav>
    <div class="abs page" style="left:340px">«</div>
    <div class="abs page" style="left:363px">1</div>
    <svg class="abs" style="left:385px;top:1055px" width="18" height="23" viewBox="0 0 18 23"><path d="M0 6L9 0l9 6v17H0z" fill="#d5490a"/><text x="9" y="17" font-family="Open Sans,sans-serif" font-size="7" fill="#fff" text-anchor="middle">2</text></svg>
    <div class="abs page" style="left:408px">3</div>
    <div class="abs page" style="left:431px">»</div>
    <div class="abs more">more &nbsp;+</div>
  </nav>
</main>

<footer>
  <div class="abs footer"></div>
  <nav class="abs foot-links">HOME &nbsp; | &nbsp; ABOUT US &nbsp; | &nbsp; CONTACT US &nbsp; | &nbsp; LIVE HELP &nbsp; | &nbsp; PRIVACY POLICY &nbsp; | &nbsp; AFFILATES &nbsp; | &nbsp; SITE MAP</nav>
  <div class="abs social" style="left:615px;background:var(--orange)"></div>
  <div class="abs social" style="left:641px;background:var(--white)"></div>
  <div class="abs social" style="left:667px;background:var(--white)"></div>
  <div class="abs copyright">All right are reserved by Quillora</div>
  <div class="abs chat-tab"></div>
  <div class="abs chat"></div>
  <svg class="abs" style="left:703px;top:1114px" width="40" height="16" viewBox="0 0 40 16"><circle cx="8" cy="8" r="7" fill="#2b2b2b"/><rect x="4" y="7" width="8" height="2" fill="#fff"/><circle cx="30" cy="8" r="7" fill="#fff"/><path d="M27 5l6 6M33 5l-6 6" stroke="#d5490a" stroke-width="1.8"/></svg>
  <div class="abs chat-input">Enter your email to Strat Chat</div>
</footer>

</body>
</html>
```